Bold & Clean Birch Harbor Stationary Design

Our company, Birch Harbor Advisory Partners needs a business card, letterhead, and envelope design that all also the formatting standards for quillpressdepot.com.

Envelope:
Safe Zone: 9.375" x 4"
Trim Size: 9.5" x 4.15"
Bleed Size: 11.125" 8.625"

Letterhead:
Safe Zone: 10.875" x 8.375"
Trim Size: 11" x 8.5"
Bleed Size: 11.125" x 8.625"

Our mailing address is:
7318 W Larkmoor Rd
Chicago, IL 60647

Please make sure the return address on the envelope is formatted correctly for mailing and the logo is not too large.

Please submit designs in word and PDF form.

Our current letterhead is attached.

We would also like a business card with our existing logo that will meet standards for formatting through Quill Press Depot (quillpressdepot.com).

These standards are:
Safe Zone: 3.375" x 1.875"
Trim Size: 3.5" x 2"
Bleed Size: 3.625" x 2.125"

The business card is going to be for Marcus Lindqvist, President/CEO of Birch Harbor Advisory Partners. Please include the Address, Telephone Number, Cell Phone Number, Fax Number, Email, and Website Address on the card, which are as follows:

7318 W Larkmoor Rd
Chicago, IL 60647

Tel: (773) 591-3072
Cell: (630) 287-6093
Fax: (63) 417-2058
Email: mjl@birchharboradvisory.com
Web: www.birchharboradvisory.com

Please make sure that we can easily change the name of the staff member and job position title ourselves as we will be having cards for individual employees in the future as well.

The back of the card should also have the Birch Harbor logo on it with our services listed:

Financial Planning | Tax | Solutions for Small Businesses

Industry/Entity Type

Accounting

Requirements
Must have
• envelope
• letterhead
• business card
• All meeting standards set out above.

```html
<!DOCTYPE html>
<html lang="en">
<head>
<meta charset="utf-8">
<title>Birch Harbor Advisory Partners — Envelope</title>
<link rel="stylesheet" href="https://fonts.googleapis.com/css2?family=Inter:wght@400;600&display=swap">
<style>
  :root {
    --backdrop: #d7d7d7;
    --paper: #f7f7f7;
    --navy: #2e3f7c;
    --orange: #ef5a2a;
    --rule: #9a9a9a;
    --edge-shadow: rgba(0,0,0,0.18);
  }
  * { margin: 0; padding: 0; box-sizing: border-box; }
  html, body {
    width: 1200px; height: 900px; overflow: hidden;
    background: var(--backdrop);
    font-family: "Inter", Arial, sans-serif;
  }
  .canvas {
    position: relative; width: 1200px; height: 900px;
  }
  .envelope {
    position: absolute; left: 220px;
    width: 760px; height: 332px;
    background: var(--paper);
    box-shadow: 0 2px 6px var(--edge-shadow);
    overflow: hidden;
  }
  .envelope--back { top: 90px; }
  .envelope--front { top: 478px; }

  /* back: closing flap */
  .envelope__flap {
    position: absolute; left: 0; top: 0;
    width: 100%; height: 112px;
    background: var(--navy);
    border-radius: 0 0 10px 10px;
    display: flex; align-items: center; justify-content: center; gap: 8px;
  }
  .envelope__web {
    color: #fff; font-size: 10px; letter-spacing: 0.02em;
  }
  .envelope__dot {
    width: 7px; height: 7px; border-radius: 50%; background: var(--orange);
  }

  /* front: brand name + return address + delivery line */
  .brand {
    position: absolute; left: 34px; top: 38px;
    display: flex; align-items: center; gap: 10px;
  }
  .brand__mark {
    width: 28px; height: 28px; border-radius: 50%;
    border: 2px solid var(--navy);
  }
  .brand__name {
    color: var(--navy); font-weight: 600; font-size: 22px; letter-spacing: -0.01em;
  }
  .delivery-line {
    position: absolute; left: 200px; right: 40px; top: 230px;
    height: 1px; background: var(--rule);
  }
  .return-address {
    position: absolute; left: 34px; bottom: 30px;
    font-size: 10px; line-height: 1.35; color: var(--navy);
    border-top: 1px solid var(--rule); padding-top: 6px;
  }
  .return-address__name { color: var(--orange); font-weight: 600; }
</style>
</head>
<body>
  <div class="canvas">
    <section class="envelope envelope--back" aria-label="Envelope back">
      <div class="envelope__flap">
        <span class="envelope__web">www.birchharboradvisory.com</span>
        <span class="envelope__dot"></span>
      </div>
    </section>

    <section class="envelope envelope--front" aria-label="Envelope front">
      <div class="brand">
        <span class="brand__mark"></span>
        <span class="brand__name">Birch Harbor</span>
      </div>
      <div class="delivery-line"></div>
      <address class="return-address" style="font-style:normal">
        <div class="return-address__name">Birch Harbor</div>
        <div>Advisory Partners</div>
        <div>7318 W Larkmoor Rd</div>
        <div>Chicago, IL 60647</div>
      </address>
    </section>
  </div>
</body>
</html>
```